Bref créative
Stationary Package for Larkmont Homes LLC
Business Card, Letterhead, envelope, fax, invoice, folder, yard marketing signage
Professional
Owen Talbert
PO Box 318264
Houston, TX 77019
larkmonthomes@quellmail.com
www.larkmonthomes.net

```html
<!DOCTYPE html>
<html lang="en">
<head>
<meta charset="utf-8">
<title>Larkmont Homes LLC – Business Card Options</title>
<link rel="stylesheet" href="https://fonts.googleapis.com/css2?family=Open+Sans:wght@400;600&family=Michroma&display=swap">
<style>
  :root {
    --board: #3a3a3a;
    --card: #ffffff;
    --accent: #e0471f;
    --accent-light: #f07a2a;
    --band-dark: #8e1d2a;
    --ink: #4a4a4a;
    --caption: #e6e6e6;
    --faint: #efefef;
  }
  * { margin: 0; padding: 0; box-sizing: border-box; }
  html, body { width: 1200px; height: 809px; overflow: hidden; }
  body { background: var(--board); font-family: "Open Sans", sans-serif; position: relative; }
  .card {
    position: absolute; width: 516px; height: 276px; background: var(--card);
    box-shadow: 0 2px 6px rgba(0,0,0,.5); overflow: hidden;
  }
  .card--front-a { left: 72px; top: 46px; }
  .card--front-b { left: 636px; top: 46px; }
  .card--back-a  { left: 72px; top: 418px; }
  .card--back-b  { left: 636px; top: 418px; }
  .band { position: absolute; left: 0; right: 0; height: 9px;
    background: linear-gradient(to bottom, var(--accent-light), var(--band-dark)); }
  .band--top { top: 0; }
  .band--bottom { bottom: 0; background: linear-gradient(to bottom, var(--band-dark), var(--accent-light)); }
  .caption {
    position: absolute; width: 516px; text-align: center; color: var(--caption);
    font-family: "Michroma", sans-serif; font-size: 14px; letter-spacing: 3px;
  }
  .caption--front-a { left: 72px; top: 354px; }
  .caption--front-b { left: 636px; top: 354px; }
  .caption--back-a  { left: 72px; top: 720px; }
  .caption--back-b  { left: 636px; top: 720px; }
  .brand {
    position: absolute; font-family: "Michroma", sans-serif; color: var(--accent);
    letter-spacing: 1px; white-space: nowrap; display: flex; align-items: center; gap: 8px;
  }
  .brand__mark { width: 12px; height: 12px; background: var(--accent); flex: none; }
  .card--front-a .brand { left: 0; right: 0; justify-content: center; top: 104px; font-size: 20px; }
  .card--front-b .brand { left: 24px; top: 132px; font-size: 13px; }
  .card--back-a .brand { left: 0; right: 0; justify-content: center; top: 96px; font-size: 20px; }
  .brand--faint { color: var(--faint); font-size: 28px; left: 0; right: 0; justify-content: center; top: 66px; letter-spacing: 2px; }
  .person { position: absolute; font-size: 10.5px; color: var(--ink); line-height: 1.6; }
  .person__name { color: var(--accent); font-size: 12px; }
  .card--front-a .person { right: 268px; top: 148px; text-align: right; }
  .card--front-b .person { left: 296px; top: 52px; }
  .contacts { position: absolute; list-style: none; font-size: 10.5px; color: var(--ink); line-height: 1.6; }
  .contacts li { display: flex; align-items: center; gap: 6px; }
  .contacts svg { width: 8px; height: 8px; flex: none; }
  .card--front-a .contacts { left: 262px; top: 148px; }
  .card--front-b .contacts { left: 296px; top: 140px; }
  .web { position: absolute; left: 0; right: 0; text-align: center; color: var(--ink);
    letter-spacing: 3px; font-size: 14px; }
  .card--back-a .web { top: 196px; }
  .card--back-b .web { top: 124px; }
</style>
</head>
<body>

<div class="card card--front-a">
  <div class="band band--top"></div>
  <div class="brand"><span class="brand__mark"></span>LARKMONT HOMES LLC</div>
  <div class="person">
    <div class="person__name">Owen Talbert</div>
    <div>President</div>
    <div>PO Box 318264 Houston,</div>
    <div>TX 77019</div>
  </div>
  <ul class="contacts">
    <li><svg viewBox="0 0 10 10"><path d="M2 1l2 2-1 1.5a6 6 0 0 0 2.5 2.5L7 6l2 2-1.5 1.5C4 9 1 6 .5 2z" fill="var(--accent)"/></svg>832-555-0146</li>
    <li><svg viewBox="0 0 10 10"><rect x="2.5" y="0.5" width="5" height="9" rx="1" fill="var(--accent)"/></svg>832-555-0186</li>
    <li><svg viewBox="0 0 10 10"><rect x="1" y="3" width="8" height="6" fill="var(--accent)"/><rect x="3" y="0.5" width="4" height="3" fill="var(--accent)"/></svg>713-555-0140</li>
    <li><svg viewBox="0 0 10 10"><circle cx="5" cy="5" r="4.5" fill="var(--accent)"/></svg>larkmonthomes@quellmail.com</li>
    <li><svg viewBox="0 0 10 10"><circle cx="5" cy="5" r="4" fill="none" stroke="var(--accent)" stroke-width="1.4"/></svg>www.larkmonthomes.net</li>
  </ul>
  <div class="band band--bottom"></div>
</div>

<div class="card card--front-b">
  <div class="band band--top"></div>
  <div class="person">
    <div class="person__name">Owen Talbert</div>
    <div>President</div>
    <div>PO Box 318264 Houston,</div>
    <div>TX 77019</div>
  </div>
  <div class="brand"><span class="brand__mark"></span>LARKMONT HOMES LLC</div>
  <ul class="contacts">
    <li><svg viewBox="0 0 10 10"><path d="M2 1l2 2-1 1.5a6 6 0 0 0 2.5 2.5L7 6l2 2-1.5 1.5C4 9 1 6 .5 2z" fill="var(--accent)"/></svg>832-555-0146</li>
    <li><svg viewBox="0 0 10 10"><rect x="2.5" y="0.5" width="5" height="9" rx="1" fill="var(--accent)"/></svg>832-555-0186</li>
    <li><svg viewBox="0 0 10 10"><rect x="1" y="3" width="8" height="6" fill="var(--accent)"/><rect x="3" y="0.5" width="4" height="3" fill="var(--accent)"/></svg>713-555-0140</li>
    <li><svg viewBox="0 0 10 10"><circle cx="5" cy="5" r="4.5" fill="var(--accent)"/></svg>larkmonthomes@quellmail.com</li>
    <li><svg viewBox="0 0 10 10"><circle cx="5" cy="5" r="4" fill="none" stroke="var(--accent)" stroke-width="1.4"/></svg>www.larkmonthomes.net</li>
  </ul>
  <div class="band band--bottom"></div>
</div>

<div class="card card--back-a">
  <div class="brand"><span class="brand__mark"></span>LARKMONT HOMES LLC</div>
  <div class="web">www.larkmonthomes.net</div>
</div>

<div class="card card--back-b">
  <div class="brand brand--faint">LARKMONT HOMES</div>
  <div class="web">www.larkmonthomes.net</div>
</div>

<div class="caption caption--front-a">BUSINESS CARD FRONT OPTION A</div>
<div class="caption caption--front-b">BUSINESS CARD FRONT OPTION B</div>
<div class="caption caption--back-a">BUSINESS CARD BACK OPTION A</div>
<div class="caption caption--back-b">BUSINESS CARD BACK OPTION B</div>

</body>
</html>
```